Bramwell Ridge Minerals

Looking for a cool, glossy business card...white with our logo on one side and then the a smaller version of the logo on the other side (top left hand corner) and then the name and position of the person next to it, and then the office address and email address on the bottom left hand corner and the phone numbers & email address on the bottom right hand corner. I have the logo already...can pass it on when you're ready.

```html
<!DOCTYPE html>
<html lang="en">
<head>
<meta charset="utf-8">
<title>Bramwell Ridge Minerals – Business Card</title>
<link rel="stylesheet" href="https://fonts.googleapis.com/css2?family=Cinzel:wght@400&family=Arimo:wght@400;700&display=swap">
<style>
  :root {
    --stage: #2b2b2d;
    --card-white: #ffffff;
    --card-black: #1c1d1f;
    --ink: #1e1e22;
    --ink-soft: #4a4a4f;
    --rule: #8a8a8e;
    --brand-blue: #1515b8;
    --brand-red: #b3121a;
    --flag-white: #e4e4e8;
    --silver: #c9c9cc;
  }
  * { box-sizing: border-box; margin: 0; padding: 0; }
  html, body {
    width: 1200px; height: 1108px; overflow: hidden;
    background: var(--stage);
  }
  .stage {
    position: relative; width: 1200px; height: 1108px;
    display: flex; justify-content: center; align-items: center; gap: 80px;
  }
  .card {
    width: 380px; height: 640px; border-radius: 22px;
    position: relative; overflow: hidden;
    box-shadow: 0 12px 30px rgba(0,0,0,.45);
  }
  .card--front {
    background: var(--card-white);
    display: flex; flex-direction: column; align-items: center;
    padding: 70px 40px 0;
  }
  .brand-art {
    width: 250px; height: 150px; border-radius: 6px;
    background: linear-gradient(160deg, var(--brand-blue) 0%, var(--brand-blue) 38%, var(--flag-white) 52%, var(--brand-red) 78%, var(--brand-red) 100%);
    opacity: .9;
  }
  .brand-name {
    font-family: "Cinzel", serif; font-weight: 400;
    color: var(--ink); text-align: center;
    font-size: 24px; letter-spacing: 1px; line-height: 1.2;
    margin-top: 14px;
  }
  .person { text-align: center; margin-top: 46px; }
  .person__name {
    font-family: "Arimo", sans-serif; font-weight: 700;
    color: var(--brand-blue); font-size: 27px; letter-spacing: .5px;
  }
  .person__role {
    font-family: "Arimo", sans-serif; font-weight: 400;
    color: var(--brand-red); font-size: 18px; margin-top: 2px;
  }
  .icon-row {
    display: flex; align-items: center; gap: 8px;
    width: 100%; margin-top: 16px;
  }
  .icon-row::before, .icon-row::after {
    content: ""; flex: 1; height: 1px; background: var(--rule);
  }
  .icon {
    width: 28px; height: 28px; border-radius: 5px;
    background: var(--brand-blue);
    display: flex; align-items: center; justify-content: center;
  }
  .contact, .address {
    font-family: "Arimo", sans-serif; color: var(--ink-soft);
    font-size: 18px; line-height: 1.35; text-align: center;
  }
  .contact { margin-top: 12px; }
  .divider { width: 80%; height: 1px; background: var(--rule); margin: 14px 0 12px; }
  .card--back {
    background: radial-gradient(ellipse at 60% 30%, #26272a 0%, var(--card-black) 70%);
    display: flex; align-items: flex-end; justify-content: center;
    padding-bottom: 120px;
  }
  .card--back .brand-name { color: var(--silver); font-size: 26px; }
</style>
</head>
<body>
<main class="stage">
  <section class="card card--front">
    <div class="brand-art" role="img" aria-label="Painted brush-stroke flag illustration in blue, white and red"></div>
    <p class="brand-name">Bramwell Ridge<br>Minerals</p>
    <div class="person">
      <p class="person__name">ELLIOT HARGROVE</p>
      <p class="person__role">Managing Director</p>
    </div>
    <div class="icon-row">
      <span class="icon" aria-label="Phone">
        <svg width="16" height="16" viewBox="0 0 16 16"><path d="M3 2h3l1 3-2 1a8 8 0 0 0 4 4l1-2 3 1v3a1 1 0 0 1-1 1A11 11 0 0 1 2 3a1 1 0 0 1 1-1z" fill="#fff"/></svg>
      </span>
      <span class="icon" aria-label="Email">
        <svg width="16" height="16" viewBox="0 0 16 16"><rect x="2" y="4" width="12" height="8" fill="none" stroke="#fff" stroke-width="1.4"/><path d="M2 4l6 5 6-5" fill="none" stroke="#fff" stroke-width="1.4"/></svg>
      </span>
      <span class="icon" aria-label="Website">
        <svg width="16" height="16" viewBox="0 0 16 16"><circle cx="8" cy="8" r="6" fill="none" stroke="#fff" stroke-width="1.4"/><ellipse cx="8" cy="8" rx="2.6" ry="6" fill="none" stroke="#fff" stroke-width="1.2"/><path d="M2 8h12" stroke="#fff" stroke-width="1.2"/></svg>
      </span>
    </div>
    <p class="contact">044-555 010 234<br>hello@bramwellridge.com<br>www.bramwellridge.com</p>
    <div class="divider"></div>
    <p class="address">88, Quarry Lane,<br>45190, Country Name</p>
  </section>
  <section class="card card--back">
    <p class="brand-name">Bramwell Ridge<br>Minerals</p>
  </section>
</main>
</body>
</html>
```